Dedicated publishing company needs Book Cover with heart and soul

I am looking for a book cover design for a lovestory named "Kellnerinnen tanzen leiser" which means "waitresses dance quieter". It´s a funny, smart and heartwarming lovestory about a couple that seems to be too diverse - but which is meant to be.
He is a young and handsome movie star and she is the interior decorator of his film sets - an "average" looking slightly older woman with the heart in the right place.
Maybe some frames to reflect her work would be nice or some hollywood decor?
We are a dedicated publishing company who cares not only for the content but also for the design and we are open to any ideas! Looking forward to seeing your designs!

Target Market(s)

Women who enjoy good love stories

Industry/Entity Type

Publishing Company

Requirements
Must have
• The title: Kellnerinnen tanzen leiser
The autors name: Petra Lindqvist

Size of front 14,8 cm wide / 21 cm high ( with additional 3 mm around), spine approx 3 cm.
Front and back design

```html
<!DOCTYPE html>
<html lang="de">
<head>
<meta charset="utf-8">
<title>Kellnerinnen tanzen leiser – Petra Lindqvist</title>
<link rel="stylesheet" href="https://fonts.googleapis.com/css2?family=Italianno&family=Cinzel:wght@700&display=swap">
<style>
  :root {
    --paper: #ffffff;
    --ink: #111111;
    --shadow-black: #0b0708;
    --plum: #5a0f2e;
    --magenta: #d4206e;
    --rose: #ea5a92;
    --blush: #f6c3d3;
    --coral: #f07148;
    --amber: #f5a233;
    --butter: #fcd56a;
    --author-top: #f8c04a;
    --author-bottom: #e8901f;
    --author-edge: #3a1d08;
  }
  html, body {
    margin: 0;
    padding: 0;
    width: 796px;
    height: 1200px;
    overflow: hidden;
    background: var(--paper);
  }
  .cover {
    position: relative;
    width: 796px;
    height: 1200px;
    background: var(--paper);
    overflow: hidden;
  }
  .cover-art {
    position: absolute;
    left: 0;
    top: 0;
    width: 796px;
    height: 960px;
    background:
      radial-gradient(ellipse 230px 200px at 420px 130px, var(--butter) 0%, var(--amber) 45%, transparent 78%),
      radial-gradient(ellipse 120px 90px at 640px 300px, var(--amber) 0%, var(--coral) 55%, transparent 85%),
      radial-gradient(ellipse 170px 140px at 160px 700px, var(--butter) 0%, var(--amber) 45%, transparent 80%),
      radial-gradient(ellipse 320px 150px at 500px 520px, var(--amber) 0%, var(--coral) 35%, var(--magenta) 70%, transparent 95%),
      radial-gradient(ellipse 200px 120px at 560px 820px, var(--blush) 0%, var(--rose) 60%, transparent 95%),
      radial-gradient(ellipse 260px 260px at 80px 260px, var(--shadow-black) 0%, var(--plum) 55%, transparent 90%),
      radial-gradient(ellipse 180px 220px at 760px 330px, var(--shadow-black) 0%, var(--plum) 60%, transparent 95%),
      linear-gradient(165deg, var(--shadow-black) 0%, var(--plum) 25%, var(--magenta) 45%, var(--coral) 65%, var(--rose) 85%, var(--blush) 100%);
    clip-path: polygon(0 0, 100% 0, 100% 63%, 82% 72%, 62% 76%, 48% 84%, 30% 88%, 12% 92%, 0 90%);
  }
  .title {
    position: absolute;
    left: 0;
    right: 0;
    top: 982px;
    margin: 0;
    text-align: center;
    font-family: "Italianno", cursive;
    font-weight: 400;
    font-size: 86px;
    line-height: 1;
    color: var(--ink);
    letter-spacing: 1px;
  }
  .author {
    position: absolute;
    left: 0;
    right: 0;
    top: 1082px;
    margin: 0;
    text-align: center;
    font-family: "Cinzel", serif;
    font-weight: 700;
    font-size: 72px;
    line-height: 1;
    letter-spacing: 1px;
    background: linear-gradient(180deg, var(--author-top), var(--author-bottom));
    -webkit-background-clip: text;
    background-clip: text;
    color: transparent;
    -webkit-text-stroke: 1.5px var(--author-edge);
  }
</style>
</head>
<body>
  <main class="cover">
    <div class="cover-art" role="img" aria-label="Posterized close-up illustration in black, pink and orange of a film star tenderly kissing a woman's hand"></div>
    <h1 class="title">“Kellnerinnen tanzen leiser”</h1>
    <p class="author">PETRA LINDQVIST</p>
  </main>
</body>
</html>
```